We require a banner design for a 53' x 10' trailer for a future development to be displayed on the side of the highway. The development name is 712 35 Commerce Park, logo is attached. This is an industrial future development. Please also include the RLW Group logo and MERO Development logos as well.

Industry/Entity Type

Real Estate / Construction / Developer / Industrial Future Development

Requirements
Must have
• Logos provided

```html
<!DOCTYPE html>
<html lang="en">
<head>
<meta charset="utf-8">
<title>Future of Industrial Development – Trailer Banner</title>
<link href="https://fonts.googleapis.com/css2?family=Outfit:wght@300;400;600;700;800&display=swap" rel="stylesheet">
<style>
  :root {
    --frame: #fce8df;
    --navy: #0d2338;
    --navy-deep: #0b1f33;
    --orange: #eda06f;
    --white: #ffffff;
    --sky: #5e7fae;
    --glow: #d7a866;
    --red: #e3202f;
    --blue: #274b9c;
  }
  html, body {
    margin: 0;
    padding: 0;
    width: 1200px;
    height: 245px;
    overflow: hidden;
    background: var(--frame);
  }
  .banner {
    position: relative;
    width: 1200px;
    height: 245px;
    background: var(--frame);
    font-family: 'Outfit', sans-serif;
  }
  .panel {
    position: absolute;
    left: 19px;
    top: 13px;
    width: 1162px;
    height: 219px;
    background: var(--navy);
    overflow: hidden;
  }
  .hero-photo {
    position: absolute;
    right: 0;
    top: 0;
    width: 620px;
    height: 100%;
    background:
      linear-gradient(90deg, var(--navy) 0%, rgba(13,35,56,0.6) 15%, rgba(13,35,56,0) 35%),
      linear-gradient(180deg, #3f5f93 0%, var(--sky) 40%, #6b6f86 62%, var(--glow) 85%, #8a7a6a 100%);
  }
  .headline {
    position: absolute;
    left: 61px;
    top: 33px;
    margin: 0;
    line-height: 0.92;
    text-transform: uppercase;
  }
  .headline-strong {
    display: block;
    color: var(--orange);
    font-weight: 700;
    font-size: 40px;
    letter-spacing: -0.2px;
  }
  .headline-light {
    display: block;
    color: var(--white);
    font-weight: 300;
    font-size: 42px;
    letter-spacing: -0.3px;
  }
  .divider {
    position: absolute;
    left: 61px;
    top: 109px;
    width: 185px;
    height: 2px;
    background: var(--white);
  }
  .partners {
    position: absolute;
    left: 61px;
    top: 130px;
    height: 60px;
    display: flex;
    align-items: center;
    gap: 26px;
    color: var(--white);
  }
  .partner {
    display: flex;
    align-items: center;
    gap: 8px;
  }
  .partner-mark {
    width: 26px;
    height: 26px;
    border-radius: 50%;
    background: var(--red);
    flex: none;
  }
  .partner-mark--square {
    border-radius: 0;
    background: var(--blue);
    width: 22px;
    height: 22px;
  }
  .partner-name {
    font-weight: 700;
    font-size: 22px;
    line-height: 1;
    white-space: nowrap;
  }
  .partner-name--park {
    font-size: 16px;
    line-height: 1.05;
  }
  .partner-name--dev {
    font-weight: 400;
    font-size: 18px;
    letter-spacing: 2px;
  }
</style>
</head>
<body>
  <main class="banner">
    <section class="panel">
      <div class="hero-photo" role="img" aria-label="Industrial refinery towers lit at dusk under a blue cloudy sky"></div>

      <h1 class="headline">
        <span class="headline-strong">Future of Industrial</span>
        <span class="headline-light">Development</span>
      </h1>
      <div class="divider"></div>

      <div class="partners">
        <div class="partner partner--group">
          <span class="partner-mark"></span>
          <span class="partner-name">RLW Group</span>
        </div>
        <div class="partner partner--park">
          <span class="partner-name partner-name--park">712 35<br>Commerce Park</span>
        </div>
        <div class="partner partner--developer">
          <span class="partner-mark partner-mark--square"></span>
          <span class="partner-name partner-name--dev">MERO Development</span>
        </div>
      </div>
    </section>
  </main>
</body>
</html>
```